MODERN + COOL Business Card Needed!

SUMMARY
This is for a 40+ year old family business that is transitioning to the 2nd generation and is in real need of a more modern facelift. Ive attached a company logo (I made quickly as an idea with my limited PSD skills) to start off with that you are welcome to change and draw ideas from. Ive also attached some screen shots of cards I like to give you an idea of my preferences.

WHAT WE DO
The company name is Tall Pine HK Ltd. But I prefer to just call it Tall Pine or Tall Pine with Hong Kong as kind of a sub heading on the business card. We own a factory as well as help our customers find factories to make their product. Product I mean, toys 99.9% of the time. Simple old school toys like board games, puzzles, wooden toys, baby/infant toys.

You can say we are a "sourcing" or "trading" or "consulting" company with a factory to help you do it. But since we deal with toys, i like to keep it modern and cool and fun, not serious like managing hedge funds.

WHAT WE ARE LOOKING FOR
A cool, unique looking business card that stands out. In terms of design, something modern and professional. I like darker colored cards and I like colors such as blue/green/dark gray, but am open to other colored themes. I Like bright lime green with gray, always though thats a nice combo. I prefer cards that are all colored and not so much white showing (I think). Ive attached a few screenshots of cards so take a look to get a feel of what I like.

We do alot of wooden stacking games in variety of colors too like Tovra, Lumo, Towerplix (google these to check them out). So designs that sort of resemble stacking or building would be cool but totally not necessary.

In terms of the physical aspects of the card, Im looking for a card a bit different than the standard rectangular shape. Double sided. Little things like having corner(s) be round or different angle instead of square edge I always thought was nice. Its got to be mostly a normal card size, no folding or smaller cards that fit weird in your wallet. No vertical designs. Am open to VERY different/creative shapes (as long as it still fits in a wallet good like a normal buisness card.
Updates

Hi everyone!

Just wanted to write a message to everyone to let them know all submissions are being reviewed or have been reviewed.  If I have not responded with feedback, rest assure your submission was definitely looked at in detail but I either have just been too busy to respond (alot of submissions!), or its on my to be considered list.

I respect and really enjoy receiving everyones creativity and work so I dont want it to go unrecognized - thus this message!  Feel free to submit more ideas if you like until this project ends.  Sometimes some designs just dont click but sometimes they can so you never know!

Thanks again for everyones participation and great work!

~Dev Orr

Target Market(s)

The cards are mainly handed to toy company sourcers and buyers. People I talk to ... say Pelvane for example... might want to make their next edition of Farthingale game with a reputable factory at a good cost so they can sell it to stores at a profit.

So these are the types of people I often try to talk and introduce myself and my company to.

Industry/Entity Type

Building

Colors
acd036
0392cd
00a88e
474747
606060

Requirements
Must have
• Just double sided, not plain rectangle corners, and just cool to look at and catches your eye!

Oh and the obvious business card stuff like place for name, address, number, email, etc.
Nice to have
• Think more modern and fun, not serious and old fashion (thats what we used to be!). Can use the logo I attached and you can definitely alter and change the logo or make a whole new one!

Oh and can definitely use a creative slogan if you like to think of one based on what I described in what we do.
Should not have
• Dont use fonts or text placement that might make "Tall Pine" look like "Tal Lpine"... We arent selling news papers!!

Please nothing related to education since we have the word Pine in the title, thats not our business at all.

Logo and design should not be too heavy on things related to toys, as though thats what we primarily focus on now, what we do may change over time.

```html
<!DOCTYPE html>
<html lang="en">
<head>
<meta charset="utf-8">
<title>Tall Pine HK Ltd. – Business Card</title>
<link rel="stylesheet" href="https://fonts.googleapis.com/css2?family=Open+Sans:wght@400;600;700&display=swap">
<style>
  :root {
    --stage: #999999;
    --lime: #afd136;
    --wood-dark: #241008;
    --wood-mid: #3a1b0d;
    --band: #4a2110;
    --white: #ffffff;
    --ink: #111111;
    --name: #5a3226;
    --role: #3b3fd2;
    --contact: #b7d93c;
    --mark: #3ab0c8;

    --blocks-rose: #d06a96;
    --blocks-steel: #9fb8d2;
    --blocks-teal: #4fbca6;
    --blocks-sky: #3cb8e0;
  }
  html, body { margin: 0; padding: 0; overflow: hidden; }
  body { width: 1200px; height: 900px; background: var(--stage); }
  .presentation { display: block; width: 1200px; height: 900px; }

  .side-tag rect { fill: url(#tagFade); }
  .side-tag text { font-family: "Open Sans", sans-serif; font-weight: 600; font-size: 30px; fill: var(--ink); }

  .lime { fill: var(--lime); }
  .band { fill: var(--band); }
  .block-stack { fill: url(#blockTones); }

  .brand-mark { fill: var(--mark); }
  .brand-name, .brand-city { font-family: "Open Sans", sans-serif; font-weight: 600; fill: var(--white); }
  .brand-name { font-size: 34px; }
  .brand-city { font-size: 30px; }

  .holder-name { font-family: "Open Sans", sans-serif; font-weight: 600; font-size: 29px; fill: var(--name); }
  .holder-role { font-family: "Open Sans", sans-serif; font-weight: 700; font-size: 14px; fill: var(--role); }
  .contact { font-family: Arial, "Open Sans", sans-serif; font-size: 17px; fill: var(--contact); text-anchor: end; }
</style>
</head>
<body>
<svg class="presentation" width="1200" height="900" viewBox="0 0 1200 900" xmlns="http://www.w3.org/2000/svg">
  <defs>
    <linearGradient id="tagFade" x1="0" x2="1" y1="0" y2="0">
      <stop offset="0" stop-color="#ffffff"/>
      <stop offset="0.6" stop-color="#eeeeee"/>
      <stop offset="1" stop-color="#9a9a9a"/>
    </linearGradient>
    <linearGradient id="woodTone" x1="0" x2="1" y1="0" y2="1">
      <stop offset="0" stop-color="var(--wood-mid)"/>
      <stop offset="0.5" stop-color="#2e150a"/>
      <stop offset="1" stop-color="var(--wood-dark)"/>
    </linearGradient>
    <linearGradient id="blockTones" x1="0" x2="1" y1="0" y2="0">
      <stop offset="0" stop-color="var(--blocks-teal)" stop-opacity="0.85"/>
      <stop offset="0.45" stop-color="var(--blocks-rose)"/>
      <stop offset="0.65" stop-color="var(--blocks-steel)"/>
      <stop offset="1" stop-color="var(--blocks-sky)" stop-opacity="0.85"/>
    </linearGradient>
    <clipPath id="cardShape">
      <rect x="140" y="15" width="706" height="405" rx="28"/>
    </clipPath>

    <g id="cardFace">
      <g clip-path="url(#cardShape)">
        <rect x="140" y="15" width="706" height="405" fill="url(#woodTone)" role="img" aria-label="Dark wood grain surface"/>
        <polygon class="lime" points="140,322 846,18 846,420 140,420"/>
        <polygon class="band" points="143,405 846,40 846,85 158,408"/>
        <rect class="block-stack" x="513" y="102" width="274" height="318" role="img" aria-label="Colourful stacked building blocks graphic"/>
      </g>
    </g>
  </defs>

  <g class="side-tag">
    <rect x="0" y="175" width="126" height="78"/>
    <text x="14" y="228">FRONT</text>
  </g>
  <g class="side-tag">
    <rect x="0" y="665" width="126" height="78"/>
    <text x="19" y="716">BACK</text>
  </g>

  <g class="card card-front">
    <use href="#cardFace"/>
    <circle class="brand-mark" cx="222" cy="97" r="30"/>
    <text class="brand-name" x="278" y="85">Tall Pine Ltd</text>
    <text class="brand-city" x="278" y="129">Hong Kong</text>
  </g>

  <g class="card card-back">
    <use href="#cardFace" transform="rotate(180 493 454)"/>
    <text class="holder-name" x="255" y="557">Your Name</text>
    <text class="holder-role" x="232" y="577">PROFESSION or POSITION</text>
    <text class="contact" x="773" y="766">Phone: +000123654897</text>
    <text class="contact" x="773" y="789">email:youremail@email.com</text>
    <text class="contact" x="773" y="813">website:www.yoursite.com</text>
  </g>
</svg>
</body>
</html>
```